Creative book cover for my dissertation on Crowdsourcing

I would like a book cover for my dissertation titled "Hivework: Swift Ample Nimble Study Methods for Making" author Marcus L. Fennwick. I am looking for something creative and fun. I would like it to use orange #FFA422 (CMYK 0, 36, 87, 0) and or blue #00A6D6 (CMYK 100, 22, 0, 16). The cover will be printed in full color and you are welcome to use other colors, images or drawn graphics. Included is a image I purchased on PixVault a few years back. For reference I have also attached a graphic used in the paper - there are several graphics of this style in the paper. I look forward to seeing your incredible design.

Target Market(s)

Industrial Designers, Designers, Students, Researchers

Requirements
Must have
• Title and author name

```html
<!DOCTYPE html>
<html lang="en">
<head>
<meta charset="utf-8">
<title>Hivework — Book Cover</title>
<link rel="stylesheet" href="https://fonts.googleapis.com/css2?family=Marcellus&family=Tinos&display=swap">
<style>
  :root {
    --stage: #f2f2f2;
    --paper: #ffffff;
    --title-blue: #1aa6d8;
    --ink: #111111;
    --crowd-dark: #5a5f63;
    --crowd-mid: #8e9498;
    --crowd-light: #c9cdd0;
  }
  html, body {
    margin: 0;
    padding: 0;
    width: 1200px;
    height: 1200px;
    overflow: hidden;
    background: var(--stage);
  }
  .canvas {
    position: relative;
    width: 1200px;
    height: 1200px;
    display: flex;
    align-items: center;
    justify-content: center;
  }
  .cover {
    width: 780px;
    height: 1100px;
    background: var(--paper);
    box-shadow: 0 6px 28px rgba(0,0,0,0.12);
    display: flex;
    flex-direction: column;
    align-items: center;
    box-sizing: border-box;
    padding-top: 110px;
  }
  .cover-title {
    margin: 0;
    font-family: "Marcellus", serif;
    font-weight: 400;
    color: var(--title-blue);
    font-size: 190px;
    line-height: 0.88;
    text-align: center;
    letter-spacing: 2px;
  }
  .cover-title span { display: block; }
  .cover-subtitle {
    margin: 34px 0 0;
    font-family: "Marcellus", serif;
    font-size: 34px;
    line-height: 1.08;
    color: var(--ink);
    text-align: center;
    letter-spacing: 1px;
    text-transform: uppercase;
  }
  .cover-subtitle span { display: block; }
  .crowd-photo {
    margin-top: 30px;
    width: 340px;
    height: 340px;
  }
  .cover-author {
    margin: 22px 0 0;
    font-family: "Tinos", serif;
    font-size: 40px;
    color: var(--ink);
    text-align: center;
  }
</style>
</head>
<body>
  <div class="canvas">
    <article class="cover">
      <h1 class="cover-title">
        <span>HIVE</span>
        <span>WORK</span>
      </h1>
      <p class="cover-subtitle">
        <span>Swift Ample</span>
        <span>Nimble Study</span>
        <span>Methods for Making</span>
      </p>
      <svg class="crowd-photo" viewBox="0 0 340 340" role="img" aria-label="Aerial photograph of a large crowd gathered in a circle, shown in a round frame">
        <defs>
          <radialGradient id="crowdTones" cx="50%" cy="50%" r="50%">
            <stop offset="0%" stop-color="var(--crowd-dark)"/>
            <stop offset="55%" stop-color="var(--crowd-mid)"/>
            <stop offset="100%" stop-color="var(--crowd-light)"/>
          </radialGradient>
        </defs>
        <circle cx="170" cy="170" r="168" fill="url(#crowdTones)"/>
      </svg>
      <p class="cover-author">Marcus L. Fennwick</p>
    </article>
  </div>
</body>
</html>
```